Bright Oak Fitness Facility Business Cards

Business Card Design that incorporates the logo and tagline

Target Market(s)

Fitness, People Who Exercise

Contact Information for Business Card

2817 Mossgrove Bend Road
Alder Falls, Oregon 97190
Phone: 352-555-Jump (5867)
www.brightoakfitness.example
info@brightoakfitness.example

Requirements
Must have
• Logo, Address, Website, email and tagline "Stronger Every Day". Colors should be red/black/grey/white

```html
<!DOCTYPE html>
<html lang="en">
<head>
<meta charset="utf-8">
<title>Bright Oak Fitness – Business Card</title>
<link rel="stylesheet" href="https://fonts.googleapis.com/css2?family=Roboto:wght@400;500;700&display=swap">
<style>
  :root {
    --stage: #2b2b2b;
    --card: #ffffff;
    --red: #ee1c25;
    --icon-red: #c8202a;
    --ink: #111111;
    --grey-text: #555555;
    --rule: #333333;
    --band-edge: #2a2a2a;
  }
  * { margin: 0; padding: 0; box-sizing: border-box; }
  html, body {
    width: 1125px; height: 1200px; overflow: hidden;
    background: var(--stage);
    font-family: "Roboto", Arial, sans-serif;
  }
  .business-card {
    position: absolute; left: 150px; top: 387px;
    width: 825px; height: 472px;
    background: var(--card);
    border-radius: 22px;
    overflow: hidden;
  }
  .brand {
    position: absolute; left: 57px; top: 136px;
    display: flex; align-items: center; gap: 14px;
  }
  .brand-dot {
    width: 26px; height: 26px; border-radius: 50%;
    background: var(--red);
  }
  .brand-name {
    font-size: 38px; font-weight: 500; color: var(--red);
    letter-spacing: 0.5px; line-height: 1;
  }
  .tagline {
    position: absolute; left: 57px; top: 260px;
    font-size: 19px; color: var(--grey-text);
  }
  .divider {
    position: absolute; left: 57px; top: 294px;
    width: 719px; height: 1px; background: var(--rule);
  }
  .person {
    position: absolute; right: 49px; top: 258px; text-align: right;
  }
  .person-name {
    font-size: 29px; font-weight: 700; color: var(--red); line-height: 1;
  }
  .person-role {
    margin-top: 11px;
    font-size: 20px; font-weight: 500; color: var(--ink); line-height: 1;
  }
  .contact-list {
    position: absolute; left: 57px; top: 351px;
    list-style: none;
  }
  .contact-list li {
    display: flex; align-items: center; gap: 10px;
    font-size: 19px; color: var(--grey-text);
    height: 26.5px;
  }
  .contact-list svg { width: 17px; height: 17px; fill: var(--icon-red); flex: none; }
  .address {
    position: absolute; right: 49px; top: 376px; text-align: right;
    font-size: 19px; color: var(--grey-text); line-height: 25px;
    font-style: normal;
  }
  .footer-band {
    position: absolute; left: 0; bottom: 0;
    width: 100%; height: 25px;
    background: var(--red);
    border-top: 3px solid var(--band-edge);
  }
</style>
</head>
<body>
  <article class="business-card">
    <div class="brand">
      <span class="brand-dot"></span>
      <span class="brand-name">Bright Oak Fitness</span>
    </div>

    <p class="tagline">Stronger Every Day</p>
    <div class="divider"></div>

    <div class="person">
      <p class="person-name">DANIEL REYES</p>
      <p class="person-role">CEO/FOUNDER</p>
    </div>

    <ul class="contact-list">
      <li>
        <svg viewBox="0 0 24 24" aria-hidden="true"><path d="M6.6 10.8a15.1 15.1 0 0 0 6.6 6.6l2.2-2.2c.3-.3.7-.4 1-.2 1.1.4 2.3.6 3.6.6.6 0 1 .4 1 1V20c0 .6-.4 1-1 1A17 17 0 0 1 3 4c0-.6.4-1 1-1h3.5c.6 0 1 .4 1 1 0 1.3.2 2.5.6 3.6.1.3 0 .7-.2 1z"/></svg>
        503-555-5867
      </li>
      <li>
        <svg viewBox="0 0 24 24" aria-hidden="true"><path d="M2 5h20v14H2zM4 7v.3l8 6 8-6V7l-8 6z"/></svg>
        info@brightoakfitness.example
      </li>
      <li>
        <svg viewBox="0 0 24 24" aria-hidden="true"><path d="M12 2a10 10 0 1 0 0 20 10 10 0 0 0 0-20zm-1 17.9A8 8 0 0 1 4.2 10.2L9 15v1a2 2 0 0 0 2 2zm6.9-2.5A2 2 0 0 0 16 16h-1v-3a1 1 0 0 0-1-1H8v-2h2a1 1 0 0 0 1-1V7h2a2 2 0 0 0 2-2v-.4a8 8 0 0 1 2.9 12.8z"/></svg>
        www.brightoakfitness.example
      </li>
    </ul>

    <address class="address">
      2817 Mossgrove Bend Road<br>
      Alder Falls, Oregon 97190
    </address>

    <div class="footer-band"></div>
  </article>
</body>
</html>
```